Bref créative
Business cards, invoice, letterhead
Stationery for baby immunisation service
Professional
Thandeka Zulani
Dr
42 9th Avenue
Brenthill
Johannesburg
drtzulani@kovahealth.co.za
PR 0738261

```html
<!DOCTYPE html>
<html lang="en">
<head>
<meta charset="utf-8">
<title>Tiny Sprouts – Business Card</title>
<link href="https://fonts.googleapis.com/css2?family=Open+Sans:wght@400;600&display=swap" rel="stylesheet">
<style>
  :root {
    --page-bg: #ece9e6;
    --card-white: #ffffff;
    --teal: #2aa6a4;
    --teal-dark: #1f8d8b;
    --leaf: #5c9f3c;
    --swoosh: #9a9591;
    --text-grey: #6f6a66;
    --taupe: #8b8079;
    --taupe-light: #a2978f;
  }
  * { box-sizing: border-box; margin: 0; padding: 0; }
  html, body {
    width: 1200px; height: 402px; overflow: hidden;
    background: var(--page-bg);
    font-family: "Open Sans", Arial, sans-serif;
  }
  .stage {
    position: relative; width: 1200px; height: 402px;
  }
  .card {
    position: absolute; top: 46px;
    width: 555px; height: 310px;
    border-radius: 16px; overflow: hidden;
    box-shadow: 0 4px 14px rgba(0,0,0,.18);
  }
  .card--front { left: 30px; background: var(--card-white); }
  .card--back { left: 615px; background: var(--taupe); }

  .card__waves { position: absolute; inset: 0; }

  .brand {
    position: absolute; left: 34px; top: 70px;
    display: flex; align-items: center; gap: 10px;
  }
  .brand__dot {
    width: 16px; height: 16px; border-radius: 50%;
    background: var(--teal);
  }
  .brand__name {
    font-size: 30px; font-weight: 600; color: var(--leaf);
    letter-spacing: -.5px;
  }
  .tagline {
    position: absolute; left: 36px; top: 116px;
    font-size: 13px; font-style: italic; color: var(--text-grey);
  }
  .holder {
    position: absolute; right: 34px; top: 42px;
    font-size: 15px; font-weight: 600; color: var(--leaf);
  }
  .contact {
    position: absolute; right: 34px; top: 186px;
    list-style: none; text-align: right;
    font-size: 12.5px; line-height: 19px; color: var(--text-grey);
  }
  .contact li { display: flex; justify-content: flex-end; align-items: center; gap: 8px; }
  .contact svg { width: 10px; height: 10px; fill: var(--text-grey); }
  .licence {
    position: absolute; right: 34px; bottom: 16px;
    font-size: 12.5px; color: #fff;
  }
  .address {
    position: absolute; left: 30px; bottom: 20px;
    font-style: normal; font-size: 13.5px; line-height: 20px; color: #fff;
  }

  .back-art {
    position: absolute; inset: 0;
    background: radial-gradient(ellipse at 68% 50%, var(--taupe-light) 0%, var(--taupe) 70%);
  }
</style>
</head>
<body>
<main class="stage">
  <section class="card card--front" aria-label="Business card front">
    <svg class="card__waves" viewBox="0 0 555 310" preserveAspectRatio="none" aria-hidden="true">
      <path d="M0 200 C150 150 330 150 555 186 L555 196 C330 164 160 170 0 214 Z" fill="var(--swoosh)" opacity=".55"/>
      <path d="M0 222 C140 196 240 220 300 262 C360 296 450 282 555 272 L555 310 L0 310 Z" fill="var(--teal)"/>
      <path d="M0 222 C140 196 240 220 300 262 C250 232 150 222 0 236 Z" fill="var(--teal-dark)" opacity=".5"/>
    </svg>

    <div class="brand">
      <span class="brand__dot"></span>
      <span class="brand__name">Tiny Sprouts</span>
    </div>
    <p class="tagline">Infancy to early childhood</p>

    <p class="holder">Dr. Thandeka Zulani</p>

    <ul class="contact">
      <li>+27 11 555 0142 <svg viewBox="0 0 10 10"><path d="M2 0h2l1 3-1.5 1a6 6 0 0 0 2.5 2.5L7 5l3 1v2a2 2 0 0 1-2 2A8 8 0 0 1 0 2a2 2 0 0 1 2-2z"/></svg></li>
      <li>+27 83 555 0178 <svg viewBox="0 0 10 10"><rect x="2.5" y="0" width="5" height="10" rx="1"/></svg></li>
      <li>drtzulani@kovahealth.co.za <svg viewBox="0 0 10 10"><path d="M0 2h10v6H0z"/></svg></li>
    </ul>

    <address class="address">42 9th Avenue<br>Brenthill, Johannesburg</address>
    <p class="licence">License No. PR 0738261</p>
  </section>

  <section class="card card--back" aria-label="Business card back">
    <div class="back-art" role="img" aria-label="White line illustration of a mother holding her baby, with a faint heart outline"></div>
  </section>
</main>
</body>
</html>
```